Scandinavian Online Sewing store need a flier

We need a 'flier' or over sized business card to include with orders which are shipped to customers. We are based in Norway and looking for something which will appeal to the Scandinavian market. The business name is 'Tråkroken' which in English means 'sewing cupboard'.

We are aiming for the younger market sector and stocking 'fresher' and 'younger' fabric, patterns and notions. (See Stitch by day, Walden+T, Harbour & Pike, Valdrine K etc.)

We would like a A5/A6 sized card which we could use in place of a business card. It should include the logo and perhaps a textured background (either paper or fabric).

Looking forward to see the ideas of all you amazingly creative souls!

Target Market(s)

Scandinavian home sewers who are interested in creating and design

Industry/Entity Type

Textile

Requirements
Must have
• logo (Attached to project) picture or artwork
Nice to have
• texture background

```html
<!DOCTYPE html>
<html lang="no">
<head>
<meta charset="utf-8">
<title>Tråkroken – flier</title>
<link rel="stylesheet" href="https://fonts.googleapis.com/css2?family=Josefin+Sans:wght@300&family=Montserrat:wght@700&family=Oswald:wght@700&display=swap">
<style>
  :root {
    --page: #f1ece4;
    --kraft: #b5a591;
    --kraft-light: #c3b4a1;
    --band: #8b7d6b;
    --band-line: #7a6c5b;
    --sage: #a9c497;
    --sage-deep: #92ad80;
    --ink: #141414;
    --paper-white: #ffffff;
    --tagline: #6a5f52;
  }
  * { box-sizing: border-box; margin: 0; padding: 0; }
  html, body { width: 1200px; height: 1000px; overflow: hidden; }
  body { background: var(--page); position: relative; }

  .flier {
    position: absolute;
    left: 160px; top: 200px;
    width: 880px; height: 600px;
    background: radial-gradient(ellipse at 40% 30%, var(--kraft-light), var(--kraft) 70%);
    overflow: hidden;
    box-shadow: 0 2px 6px rgba(0,0,0,.18);
  }
  .fabric-band {
    position: absolute;
    left: 0; right: 0; top: 380px; height: 150px;
    background: repeating-linear-gradient(0deg, var(--band) 0 3px, var(--band-line) 3px 5px);
  }
  .brand-panel {
    position: absolute;
    left: 52px; top: 70px;
    width: 300px; height: 480px;
    background: var(--sage);
    padding: 34px 24px 24px;
  }
  .brand-name {
    font-family: "Oswald", sans-serif;
    font-weight: 700;
    font-size: 52px;
    line-height: 1;
    letter-spacing: 1px;
    color: var(--paper-white);
    text-transform: uppercase;
  }
  .notions-artwork {
    margin-top: 22px;
    width: 252px; height: 340px;
    background: linear-gradient(160deg, var(--sage-deep), var(--sage));
  }
  .tagline {
    position: absolute;
    left: 470px; top: 100px;
    font-family: "Josefin Sans", sans-serif;
    font-weight: 300;
    font-size: 38px;
    line-height: 1.3;
    color: var(--tagline);
  }
  .web-address {
    position: absolute;
    right: 60px; top: 318px;
    font-family: "Montserrat", sans-serif;
    font-weight: 700;
    font-size: 26px;
    color: var(--ink);
  }
  .thread-frame { position: absolute; inset: 0; pointer-events: none; }
</style>
</head>
<body>
  <article class="flier">
    <div class="fabric-band"></div>

    <section class="brand-panel">
      <p class="brand-name">Tråkroken</p>
      <div class="notions-artwork" role="img" aria-label="Illustration of sewing notions: thread spools, tape measure, scissors, pincushion and buttons"></div>
    </section>

    <p class="tagline">fristelser<br>for de som<br>elsker å skaper</p>
    <p class="web-address">www.trakroken.no</p>

    <svg class="thread-frame" viewBox="0 0 880 600" aria-hidden="true">
      <g fill="none" stroke="var(--ink)" stroke-width="3" stroke-linecap="round">
        <path d="M60 60 C300 48 600 44 830 58 C840 200 842 400 836 545 C600 556 300 560 70 548 C62 400 58 200 60 60"/>
        <path d="M44 72 C300 64 600 62 846 70 C850 250 846 420 850 560 C600 570 280 566 50 562 C44 400 40 220 44 72"/>
        <path d="M72 48 C320 38 620 36 820 46 C828 220 832 420 824 530"/>
        <path d="M760 60 C790 40 800 80 770 76"/>
        <path d="M836 545 C846 520 858 540 842 552"/>
      </g>
    </svg>
  </article>
</body>
</html>
```